Real estate website

Please find attached a rough outline of what we want for the design. This is just for placement to show what to have on the menu's as content, etc. but please make it look much more professional.
Please make the bottom footer a similar gradient to the logo
Please make the sign up now and log in buttons look better - these are just samples to show placement
Please use the correct logos for dwelloria.com.au, plotnex.com.au and roofquill.com.au
Where it has 'video embed' just leave that as is as we will replace that with a video.

```html
<!DOCTYPE html>
<html lang="en">
<head>
<meta charset="utf-8">
<title>Keyline Direct – Sell or Rent Privately</title>
<link href="https://fonts.googleapis.com/css2?family=Nunito:wght@400;600;700&family=Poppins:wght@600;800&display=swap" rel="stylesheet">
<style>
:root{
  --green-dark:#137a3a;
  --green:#1e8a3a;
  --lime:#8cc63f;
  --ink:#1d1d1d;
  --text:#333;
  --bg:#f4f3f4;
  --white:#fff;
  --line:#8a8a8a;
}
*{box-sizing:border-box;margin:0;padding:0}
html,body{width:1200px;height:648px;overflow:hidden}
body{font-family:"Nunito",sans-serif;background:var(--bg);color:var(--text);position:relative}
.site-header{position:absolute;top:0;left:0;width:1200px;height:56px;background:var(--white);box-shadow:0 2px 6px rgba(0,0,0,.05)}
.brand{position:absolute;left:17px;top:15px;display:flex;align-items:center;gap:8px;font-size:17px;color:#444}
.brand-mark{width:22px;height:22px;border-radius:50%;background:var(--green)}
.main-nav{position:absolute;left:284px;top:17px;display:flex;gap:26px}
.main-nav a{display:flex;align-items:center;gap:8px;font-size:12px;color:#222;text-decoration:none;letter-spacing:.2px}
.main-nav svg{width:18px;height:18px}
.btn{position:absolute;top:13px;height:30px;display:flex;align-items:center;justify-content:center;color:#fff;font-family:"Poppins",sans-serif;font-weight:600;font-size:11px;letter-spacing:.3px;background:linear-gradient(90deg,var(--green-dark),var(--lime))}
.btn-signup{left:977px;width:112px}
.btn-login{left:1104px;width:73px}

.hero-art{position:absolute;left:0;top:56px;width:440px;height:547px}
.presenter{position:absolute;left:52px;top:41px;width:288px;height:443px;border-radius:140px 140px 6px 6px;background:linear-gradient(180deg,#b89a86 0%,#3a3a3a 30%,#1f1f1f 100%)}
.video-label{position:absolute;left:165px;top:487px;transform:rotate(-27deg);font-size:14px;color:#222}

.pitch{position:absolute;left:372px;top:118px;width:392px;text-align:center}
.pitch h1{font-family:"Poppins",sans-serif;font-weight:800;font-size:22px;color:var(--ink);letter-spacing:-.2px}
.ask{margin-top:16px;display:flex;align-items:center;justify-content:center;gap:8px;font-size:22px;color:var(--ink);letter-spacing:.5px}
.ask svg{width:30px;height:30px}
.ask strong{font-family:"Poppins",sans-serif;font-weight:800;color:var(--green)}
.pitch p{margin-top:24px;font-size:10.5px;line-height:15.6px;color:#333}
.cta-outline{position:absolute;left:484px;top:361px;width:215px;height:37px;border:1px solid var(--lime);display:flex;align-items:center;justify-content:center;font-size:14px;font-weight:600;color:var(--ink);background:transparent}
.portals{position:absolute;left:372px;top:444px;width:392px;height:58px;display:flex;align-items:center}
.portal{flex:1;display:flex;align-items:center;justify-content:center;gap:5px;font-size:13px;font-weight:700;color:#333}
.portal+.portal{border-left:1px solid #bbb;height:58px}
.portal .dot{width:10px;height:10px;border-radius:50%;background:#e4002b}
.portal.p2{color:var(--green)}
.portal.p3{color:#c8102e}

.guide-card{position:absolute;left:805px;top:97px;width:365px;height:453px;background:var(--white);box-shadow:0 0 8px rgba(0,0,0,.04)}
.guide-card h2{margin-top:30px;text-align:center;font-family:"Poppins",sans-serif;font-weight:800;font-size:23px;color:var(--green)}
.guide-card .sub{text-align:center;font-size:15px;color:#222;margin-top:2px}
.field{position:absolute;left:28px;width:316px;height:38px;border:1px solid #777;font-size:10px;color:#222;padding-left:12px;display:flex;align-items:center}
.captcha{position:absolute;left:28px;top:319px;width:172px;height:43px;border:1px solid #ddd;border-radius:2px;background:#f9f9f9;display:flex;align-items:center;padding-left:8px;gap:9px;font-size:7.5px;color:#222}
.captcha .box{width:15px;height:15px;border:2px solid #c1c1c1;border-radius:2px;background:#fff}
.captcha .meta{margin-left:auto;margin-right:7px;text-align:center;font-size:5px;color:#666;line-height:7px}
.captcha .meta i{display:block;width:14px;height:14px;margin:0 auto 2px;border-radius:50%;background:#4a90e2}
.submit{position:absolute;left:28px;top:380px;width:316px;height:47px;background:linear-gradient(90deg,var(--green-dark),var(--lime));color:#fff;font-family:"Poppins",sans-serif;font-weight:800;font-size:18px;display:flex;align-items:center;justify-content:center}

.site-footer{position:absolute;left:0;top:603px;width:1200px;height:45px;background:linear-gradient(90deg,var(--green-dark),var(--lime));color:#fff;font-size:11.5px}
.site-footer span{position:absolute;top:15px}
</style>
</head>
<body>
<header class="site-header">
  <div class="brand"><span class="brand-mark"></span>Keyline Direct</div>
  <nav class="main-nav">
    <a href="#"><svg viewBox="0 0 20 20" fill="none" stroke="#1e8a3a" stroke-width="1.3"><path d="M3 9 10 3l7 6v8H3z"/><circle cx="10" cy="12" r="3"/></svg>SELL MY PROPERTY</a>
    <a href="#"><svg viewBox="0 0 20 20" fill="none" stroke="#1e8a3a" stroke-width="1.3"><circle cx="13" cy="7" r="4"/><path d="M10 10 3 17m2-2 2 2"/></svg>RENT MY PROPERTY</a>
    <a href="#"><svg viewBox="0 0 20 20" fill="none" stroke="#1e8a3a" stroke-width="1.3"><circle cx="10" cy="10" r="8"/><path d="M6 10l4-3 4 3v4H6z"/></svg>RENTAL MANAGEMENT</a>
  </nav>
  <a class="btn btn-signup">SIGN UP NOW</a>
  <a class="btn btn-login">LOGIN</a>
</header>

<section class="hero-art">
  <svg width="440" height="547" viewBox="0 0 440 547">
    <defs><linearGradient id="tri" x1="0" y1="1" x2="1" y2="0"><stop offset="0" stop-color="#137a3a"/><stop offset="1" stop-color="#8cc63f"/></linearGradient></defs>
    <polygon points="31,121 431,321 31,520" fill="url(#tri)"/>
  </svg>
  <div class="presenter" role="img" aria-label="Presenter video placeholder – man in dark suit speaking"></div>
  <svg style="position:absolute;left:0;top:0" width="440" height="547"><polygon points="97,490 440,320 440,547 97,547" fill="#f4f3f4"/></svg>
  <div class="video-label">Video Embed</div>
</section>

<section class="pitch">
  <h1>WANT TO PAY NOTHING UPFRONT?</h1>
  <div class="ask"><svg viewBox="0 0 30 30" fill="none" stroke="#1e8a3a" stroke-width="1.4"><path d="M5 8c0 9 7 17 16 17l3-4-4-3-2 2c-3-1-6-4-7-7l2-2-3-4z"/><circle cx="22" cy="7" r="5"/></svg>ASK US HOW – <strong>0412555019</strong></div>
  <p>Listing a house in Australia for sale or rental is costly! In the ACT, it's even worse! ACT residents are paying more to list and sell online, than in other parts of Australia. Keyline Direct solves this problem for you. Sell or rent your own home privately in the ACT with Keyline Direct and pay zero commission. You'll be listed for an unlimited time on all the major sites. All the tools for listing are inside your account, sign up today and get started.</p>
</section>
<div class="cta-outline">Sell with No Commission on</div>
<div class="portals">
  <div class="portal p1"><span class="dot"></span>dwelloria.com.au</div>
  <div class="portal p2">plotnex.com.au</div>
  <div class="portal p3">roofquill.com.au</div>
</div>

<aside class="guide-card">
  <h2>GET YOUR FREE GUIDE</h2>
  <div class="sub">To Listing Privately in the act</div>
  <div class="field" style="top:110px">Email</div>
  <div class="field" style="top:162px">First name</div>
  <div class="field" style="top:214px">Last name</div>
  <div class="field" style="top:266px">Phone Number</div>
  <div class="captcha"><span class="box"></span>I'm not a robot<div class="meta"><i></i>VerifyBox<br>Privacy · Terms</div></div>
  <div class="submit">SUBMIT</div>
</aside>

<footer class="site-footer">
  <span style="left:258px">FINANCE</span>
  <span style="left:331px">CONVERANCING</span>
  <span style="left:452px">BUILDING INSPECTION</span>
  <span style="left:606px">PEST INSPECTION</span>
  <span style="left:734px">VALUATION</span>
  <span style="left:820px">MARKET APPARAISAL</span>
  <span style="left:1163px">X37</span>
</footer>
</body>
</html>
```